Brochure Design Project

I would like for it took look a little different than my website, elegant, and classy. Our company wants to draw upper class customers to care for their home. We also focus private water taxi services for businesses to taxi their employees.

Target Market(s)

tourists, seasonal residents, property management.

Industry/Entity Type

Professional Service

Font styles to use
Serif

Requirements
Must have
• 2 sides

```html
<!DOCTYPE html>
<html lang="en">
<head>
<meta charset="utf-8">
<title>Harborlight Concierge Services – Trifold Brochure</title>
<link rel="stylesheet" href="https://fonts.googleapis.com/css2?family=Source+Sans+3:wght@400;600;700&family=Cinzel:wght@400&family=Bebas+Neue&display=swap">
<style>
  :root{
    --stage:#444444;
    --paper:#ffffff;
    --panel-light:#f1f0f1;
    --panel-dark:#3a3a3a;
    --panel-dark-hi:#5a5a5a;
    --accent:#c8692e;
    --ink:#2b2b2b;
    --wood:#4a3c31;
    --wood-dark:#2f2620;
    --white:#ffffff;
  }
  *{box-sizing:border-box;margin:0;padding:0}
  html,body{width:1200px;height:1200px;overflow:hidden;background:var(--stage)}
  body{font-family:"Source Sans 3",Arial,sans-serif;color:var(--ink)}
  .brochure{position:absolute;left:90px;top:204px;width:1021px;height:793px;background:var(--paper);display:flex}
  .panel{position:relative;height:100%}
  .panel--about{width:338px}
  .panel--center{width:334px}
  .panel--cover{width:349px}
  .block{position:absolute;left:0;width:100%}
  .about{top:0;height:412px;background:var(--panel-light);padding:32px 38px 0 28px}
  .bio{top:412px;height:381px;background:var(--paper);padding:21px 42px 0 28px}
  .rule{width:118px;height:3px;background:var(--ink);margin-bottom:16px}
  h2{font-size:15px;font-weight:600;color:var(--accent);letter-spacing:.01em;margin-bottom:13px}
  h2.spaced{margin-top:22px}
  .bio h2{margin-bottom:5px}
  p{font-size:12.4px;line-height:15.1px;text-align:justify;hyphens:auto}
  .bio p{position:relative;z-index:1}
  .photo{position:absolute;left:0;width:100%}
  .photo--boat{bottom:0;height:140px;background:linear-gradient(to bottom,var(--paper) 0%,#d9d9d9 40%,#8f8f8f 72%,#5d5d5d 100%)}
  .photo--bell{top:0;height:338px;background:radial-gradient(ellipse at 50% 48%,#d8d8d8 0%,#8d8d8d 28%,#3b3430 62%,#5b3a22 100%)}
  .title-band{top:338px;height:72px;background:linear-gradient(90deg,var(--panel-dark) 0%,var(--panel-dark-hi) 50%,var(--panel-dark) 100%);display:flex;align-items:center;justify-content:center}
  .title-band span{color:var(--white);font-size:14.4px;font-weight:600;letter-spacing:-.01em}
  .intro{top:410px;height:187px;background:var(--panel-light);padding:37px 31px 0 21px}
  .contact{top:597px;height:196px;background:linear-gradient(90deg,var(--panel-dark) 0%,var(--panel-dark-hi) 50%,var(--panel-dark) 100%);color:var(--white);text-align:center;padding-top:21px}
  .contact .lead,.contact .closing{font-size:12.4px;font-weight:700;line-height:15.3px}
  .contact .phone{font-size:29px;font-weight:700;color:var(--accent);margin:7px 0 9px;letter-spacing:.01em}
  .photo--sunset{top:0;height:575px;background:linear-gradient(to bottom,#e08a2a 0%,#d9782a 9%,#9a7a5c 20%,#6f6a66 40%,#5c5d63 62%,#2c3040 85%,#262a36 100%)}
  .gap{top:575px;height:22px;background:var(--paper)}
  .brand{top:597px;height:196px;background:linear-gradient(180deg,var(--wood) 0%,var(--wood-dark) 100%);color:var(--white);text-align:center;padding-top:22px}
  .brand .mark{width:40px;height:40px;border:2px solid var(--white);border-radius:50%;margin:0 auto 24px}
  .brand .name{font-size:21px;font-weight:400;letter-spacing:.17em;line-height:39px;text-transform:uppercase}
  .headline{position:absolute;left:27px;top:153px;width:297px;height:185px}
  .headline svg{position:absolute;left:0;top:0}
  .headline .line{position:absolute;left:0;width:100%;text-align:center;color:var(--white)}
  .headline .l1{top:-22px;font-family:"Cinzel",Georgia,serif;font-size:44px}
  .headline .l2{top:42px;font-family:"Cinzel",Georgia,serif;font-size:35px;letter-spacing:.01em}
  .headline .l3{top:86px;font-family:"Bebas Neue",Impact,sans-serif;font-size:72px;line-height:72px;letter-spacing:.005em}
</style>
</head>
<body>
<div class="brochure">

  <section class="panel panel--about">
    <div class="block about">
      <h2>ABOUT US</h2>
      <p>Founded in 2017 by Daniel and Claire Whitmore, Harborlight Concierge provides the Pine Island area with an exclusive list of services for property management including home services, rental guest liaison, and membership services. We are also offer private charters for water transportation to barrier islands, exclusive fishing adventures, and sightseeing tours.</p>
      <h2 class="spaced">CLAIRE WHITMORE</h2>
      <p>As co-owner and operator of Harborlight Concierge, Claire combines her strong professional background in healthcare with a passion in caring for people in the community. Born and raised in Florida, Claire graduated from a local university with a Bachelor’s Degree in Science Nursing. With years of business experience within the largest healthcare system in the state, she has held extraordinary positions that involve utilization management and centralized solutions. During her free time, she enjoys fishing, and boating with her family.</p>
    </div>
    <div class="block bio">
      <div class="rule"></div>
      <h2>DANIEL WHITMORE</h2>
      <p>With a strong corporate background and well-known experience working with one of the largest power and energy companies in the world, Daniel knows the importance of providing top level customer service. Also born and raised in Florida, Daniel completed an apprenticeship program in Miami where he earned his title as a Line Specialist. Now retired, throughout the years he continued to peruse his passion for competitive sports fishing where he developed long standing professional relationships within his community.</p>
      <div class="photo photo--boat" role="img" aria-label="Black and white photo of a sport fishing yacht cruising past a jetty"></div>
    </div>
  </section>

  <section class="panel panel--center">
    <div class="photo photo--bell" role="img" aria-label="Close-up photo of a chrome hotel service bell on a polished counter"></div>
    <div class="block title-band"><span>HARBORLIGHT CONCIERGE SERVICES L.L.C.</span></div>
    <div class="block intro">
      <p>Serving Bokeelia and surrounding sister islands, Harborlight concierge is the top innovator in the concierge service industry. Concierge services are tailored to each request ensuring an exceptional client experience. We have the knowledge and resources through our trusted network of service providers to meet your individual needs and preferences.</p>
    </div>
    <div class="block contact">
      <div class="lead">Submit a request on our website HCSatYour<br>Request.com or Call and speak with<br>a concierge specialist</div>
      <div class="phone">(555) 014-2017</div>
      <div class="closing">Concierge Services Have Grown Far Beyond<br>That of A Hotel Lobby.<br>Call Us With Your Request And HCS Will Do The Rest!</div>
    </div>
  </section>

  <section class="panel panel--cover">
    <div class="photo photo--sunset" role="img" aria-label="Photo of a boat wake on open water at sunset, seen from the stern"></div>
    <div class="headline">
      <svg width="297" height="185" viewBox="0 0 297 185" aria-hidden="true">
        <path d="M47 1.5 H1.5 V183.5 H295.5 V1.5 H250" fill="none" stroke="#ffffff" stroke-width="2.5"/>
      </svg>
      <div class="line l1">YOUR</div>
      <div class="line l2">REQUEST IS</div>
      <div class="line l3">OUR DEMAND</div>
    </div>
    <div class="block gap"></div>
    <div class="block brand">
      <div class="mark"></div>
      <div class="name">Harborlight Concierge<br>Services L.L.C.</div>
    </div>
  </section>

</div>
</body>
</html>
```